Brivane - Business Cards for a new venture

create business card for a startup classified business dealing in construction materials, the cards need to have a professional look but modern, more serious than playful, one of the samples must include the official font (attached), please explore using the official colors in the company's logo

Target Market(s)

Energy sector

Contact Information for Business Card

Font styles to use
Other font styles liked:
• suissnord

Requirements
Must have
• corporate colors (in logo attached)
Nice to have
• Official font (in one of the samples) font is : suissnord
Should not have
• Cartoonish look

```html
<!DOCTYPE html>
<html lang="en">
<head>
<meta charset="utf-8">
<title>Brivane Business Card</title>
<link href="https://fonts.googleapis.com/css2?family=Arimo:wght@400;700&family=Michroma&display=swap" rel="stylesheet">
<style>
  :root {
    --stage: #2e2a28;
    --card-white: #ffffff;
    --card-shade: #f1f1f1;
    --brand-blue: #0d4a86;
    --brand-blue-deep: #063462;
    --text-grey: #555a60;
    --rule-grey: #d4d6d8;
    --back-text: #dfe6ee;
  }
  * { box-sizing: border-box; margin: 0; padding: 0; }
  html, body { width: 1200px; height: 844px; overflow: hidden; }
  body {
    background: var(--stage);
    font-family: "Arimo", Arial, sans-serif;
    position: relative;
  }
  .card {
    position: absolute;
    top: 272px;
    width: 540px;
    height: 300px;
    border-radius: 3px;
    overflow: hidden;
    box-shadow: 0 6px 18px rgba(0,0,0,0.35);
  }
  /* Front */
  .card-front {
    left: 30px;
    background: linear-gradient(135deg, var(--card-white) 40%, var(--card-shade));
  }
  .front-band {
    position: absolute; left: 0; right: 0; bottom: 0; height: 12px;
    background: var(--brand-blue);
  }
  .brand-mark {
    position: absolute; left: 40px; top: 112px; width: 200px;
    display: flex; align-items: center; gap: 10px;
    color: var(--brand-blue);
    font-family: "Michroma", sans-serif;
    font-size: 24px; letter-spacing: 2px;
  }
  .brand-mark .dot {
    width: 12px; height: 12px; border-radius: 50%; background: var(--brand-blue); flex: none;
  }
  .divider {
    position: absolute; left: 262px; top: 36px; width: 1px; height: 170px;
    background: linear-gradient(var(--card-white), var(--rule-grey) 30%, var(--rule-grey) 70%, var(--card-white));
  }
  .contact { position: absolute; left: 290px; top: 56px; }
  .person-name {
    color: var(--brand-blue); font-weight: 700; font-size: 19px; letter-spacing: 0.3px;
  }
  .person-title { color: var(--text-grey); font-size: 14px; margin-top: 1px; }
  .contact-list { list-style: none; margin-top: 12px; }
  .contact-list li {
    display: flex; align-items: center; gap: 6px;
    color: var(--text-grey); font-size: 14px; line-height: 18px;
  }
  .contact-list svg { width: 13px; height: 13px; flex: none; fill: var(--brand-blue-deep); }
  .address {
    position: absolute; left: 70px; bottom: 48px;
    color: var(--text-grey); font-size: 16px; letter-spacing: 0.2px;
  }
  /* Back */
  .card-back {
    left: 630px;
    background: linear-gradient(160deg, var(--brand-blue) 0%, var(--brand-blue-deep) 100%);
    display: flex; flex-direction: column; align-items: center; justify-content: center;
    gap: 26px;
  }
  .back-name {
    font-family: "Michroma", sans-serif; color: var(--back-text);
    font-size: 34px; letter-spacing: 5px; margin-top: -30px;
  }
  .back-web {
    font-family: "Michroma", sans-serif; color: var(--back-text);
    font-size: 13px; letter-spacing: 3px;
  }
</style>
</head>
<body>
  <section class="card card-front">
    <div class="brand-mark"><span class="dot"></span><span>BRIVANE</span></div>
    <div class="divider"></div>
    <div class="contact">
      <div class="person-name">DANIEL HARPER</div>
      <div class="person-title">Managing Director</div>
      <ul class="contact-list">
        <li><svg viewBox="0 0 16 16"><path d="M2 6c0-2 2-3 6-3s6 1 6 3v1h-3V6H5v1H2zM4 8h8l2 5H2z"/></svg>044-210 387 654</li>
        <li><svg viewBox="0 0 16 16"><path d="M4 1h8a1 1 0 0 1 1 1v12a1 1 0 0 1-1 1H4a1 1 0 0 1-1-1V2a1 1 0 0 1 1-1zm1 2v9h6V3z"/></svg>044-210 387 655</li>
        <li><svg viewBox="0 0 16 16"><path d="M1 3h14v10H1zm1.5 1.5L8 9l5.5-4.5z"/></svg>info@brivane.com</li>
      </ul>
    </div>
    <div class="address">12345, Address Goes Here Country Name, 123456.</div>
    <div class="front-band"></div>
  </section>

  <section class="card card-back">
    <div class="back-name">BRIVANE</div>
    <div class="back-web">WWW.BRIVANE.COM</div>
  </section>
</body>
</html>
```